Business Cards for Life Coaching Practice
RVT Harbor Ltd
Business Cards for Life Coaching Practice - Consulting
Creative Brief
Professional
Dovinder Plume
admin@rvtharbor.co.uk
brightpathmentoring.co.uk
Please show me both 1 side and 2 sided options. I have uploaded logo files and would like to see design options using the colour schemes.
"Be True To Yourself" ------Your Journey-------
RVTHARBOR RVTHARBOR
please only send me designs on plastic cards.
sevensky sevensky
Its Done! check your private messages on top right side messages (1) thanks!
#33 please can you provide different colour backgrounds for this design?
Its Done! thanks
#32 Please apply this back to designs #23 - #25 and #27 - #29
#22 the blue stone is too big for the card and needs to be smaller to fit on the card
#14 I like the plastic shine type card. As stated i would like the statement on back and stones need to be on card
#7 I like the wave concept. The back is however too dark and I want "be true to yourself" on the back.

```html
<!DOCTYPE html>
<html lang="en">
<head>
<meta charset="utf-8">
<title>RVT Harbor Ltd — Business Cards</title>
<link rel="stylesheet" href="https://fonts.googleapis.com/css2?family=Cinzel:wght@400&family=Cormorant+SC:wght@500&display=swap">
<style>
  :root {
    --backdrop: #eceef1;
    --card: #ffffff;
    --brand-blue: #1f5fa8;
    --deep-blue: #1b3f77;
    --sky: #bcd6e8;
    --stone: #d3e4ef;
    --rule: #b9c2cc;
    --ink: #2b3a4e;
    --silver: #dfe3e8;
  }
  * { margin: 0; padding: 0; box-sizing: border-box; }
  html, body { width: 1200px; height: 874px; overflow: hidden; background: var(--backdrop); }
  .canvas { position: relative; width: 1200px; height: 874px; }

  .card {
    position: absolute;
    background: var(--card);
    border-radius: 22px;
    box-shadow: 0 6px 18px rgba(40, 60, 90, 0.16);
    overflow: hidden;
  }

  /* Back */
  .card--back { left: 620px; top: 90px; width: 500px; height: 286px; }
  .back-mark { position: absolute; left: 120px; top: 60px; width: 120px; height: 120px; border-radius: 50%; background: var(--stone); }
  .back-name {
    position: absolute; left: 258px; top: 146px;
    font-family: "Cinzel", serif; font-weight: 400; font-size: 26px; line-height: 1;
    color: var(--brand-blue); letter-spacing: 1px; white-space: nowrap;
  }

  /* Front */
  .card--front { left: 80px; top: 450px; width: 520px; height: 297px; }
  .logo { position: absolute; left: 24px; top: 30px; display: flex; align-items: center; gap: 10px; }
  .logo-dot { width: 30px; height: 30px; border-radius: 50%; background: var(--sky); flex: none; }
  .logo-name { font-family: "Cinzel", serif; font-weight: 400; font-size: 22px; line-height: 1; color: var(--brand-blue); letter-spacing: 0.5px; white-space: nowrap; }
  .logo-rule { position: absolute; left: 64px; top: 66px; width: 150px; height: 1px; background: var(--rule); }

  .holder {
    position: absolute; right: 40px; top: 30px;
    font-family: "Cinzel", serif; font-weight: 400; font-size: 19px; line-height: 1; color: var(--deep-blue); white-space: nowrap;
  }
  .holder-rule { position: absolute; left: 232px; top: 58px; width: 268px; height: 1px; background: var(--rule); }
  .holder-tab { position: absolute; left: 500px; top: 20px; width: 20px; height: 38px; background: var(--brand-blue); }

  .contacts { position: absolute; left: 22px; top: 188px; list-style: none; }
  .contacts li {
    display: flex; align-items: center; gap: 6px; height: 15px;
    font-family: "Cormorant SC", serif; font-weight: 500; font-size: 12px; color: var(--ink); white-space: nowrap;
  }
  .contacts svg { width: 10px; height: 10px; flex: none; }

  .swoosh { position: absolute; left: 0; bottom: 0; width: 520px; height: 60px; }
</style>
</head>
<body>
<main class="canvas">

  <section class="card card--back" aria-label="Card back">
    <div class="back-mark"></div>
    <p class="back-name">RVT HARBOR</p>
  </section>

  <section class="card card--front" aria-label="Card front">
    <div class="logo">
      <span class="logo-dot"></span>
      <span class="logo-name">RVT HARBOR</span>
    </div>
    <div class="logo-rule"></div>

    <p class="holder">Dovinder Plume</p>
    <div class="holder-rule"></div>
    <div class="holder-tab"></div>

    <ul class="contacts">
      <li>
        <svg viewBox="0 0 10 10"><circle cx="5" cy="5" r="5" fill="#2b3a4e"/><path d="M3.2 2.6l1 .9-.5.8a4 4 0 0 0 2 2l.8-.5.9 1-.7.8C4.8 7.3 2.7 5.2 2.5 3.3z" fill="#fff"/></svg>
        020 7946 0182
      </li>
      <li>
        <svg viewBox="0 0 10 10"><circle cx="5" cy="5" r="5" fill="#2b3a4e"/><rect x="3.5" y="2.2" width="3" height="5.6" rx="0.6" fill="#fff"/></svg>
        07700 900 315
      </li>
      <li>
        <svg viewBox="0 0 10 10"><circle cx="5" cy="5" r="5" fill="#2b3a4e"/><rect x="2.5" y="3.3" width="5" height="3.4" fill="#fff"/><path d="M2.5 3.3L5 5.2 7.5 3.3" stroke="#2b3a4e" stroke-width="0.5" fill="none"/></svg>
        admin@rvtharbor.co.uk
      </li>
      <li>
        <svg viewBox="0 0 10 10"><circle cx="5" cy="5" r="5" fill="#2b3a4e"/><circle cx="5" cy="5" r="2.6" stroke="#fff" stroke-width="0.6" fill="none"/><path d="M2.4 5h5.2M5 2.4v5.2" stroke="#fff" stroke-width="0.5"/></svg>
        www.rvtharborcoaching.co.uk
      </li>
    </ul>

    <svg class="swoosh" viewBox="0 0 520 60" preserveAspectRatio="none">
      <path d="M0 30 L330 30 L350 40 L520 40 L520 60 L0 60 Z" fill="var(--silver)"/>
      <path d="M0 36 L320 36 L345 46 L520 46 L520 50 L340 50 L315 40 L0 40 Z" fill="var(--deep-blue)"/>
      <path d="M0 45 L300 45 L330 55 L520 55 L520 57 L325 57 L296 48 L0 48 Z" fill="var(--brand-blue)"/>
    </svg>
  </section>

</main>
</body>
</html>
```